Page for a flyer

I need a page designed that is 8.5" wide and 5.5" height. I need the left half of the page to be vintage looking in color and texture and the other half to be plain white and look like it is ripped down the middle

```html
<!DOCTYPE html>
<html lang="en">
<head>
<meta charset="UTF-8">
<title>Flyer Page – Vintage Torn Half</title>
<link rel="stylesheet" href="https://fonts.googleapis.com/css2?family=Lora&display=swap">
<style>
  :root {
    --page-white: #ffffff;
    --paper-cream: #efe7d8;
    --paper-light: #f3ede2;
    --paper-warm: #e4d7c0;
    --paper-sepia: #b9a27a;
    --ray-blue: #a9c4c6;
    --ray-blue-deep: #8db0b4;
    --edge-rim: #d8c7a6;
    --edge-shadow: rgba(70, 55, 30, 0.4);
  }
  * { margin: 0; padding: 0; box-sizing: border-box; }
  html, body {
    width: 1200px;
    height: 756px;
    overflow: hidden;
    background: var(--page-white);
    font-family: "Lora", serif;
  }
  .flyer-page {
    position: relative;
    width: 1200px;
    height: 756px;
    background: var(--page-white);
  }
  .vintage-half {
    position: absolute;
    left: 0;
    top: 0;
    width: 620px;
    height: 756px;
    filter: drop-shadow(2px 1px 1.5px var(--edge-shadow));
  }
  .stop-cream { stop-color: var(--paper-cream); }
  .stop-light { stop-color: var(--paper-light); }
  .stop-warm { stop-color: var(--paper-warm); }
  .stop-blue { stop-color: var(--ray-blue); stop-opacity: 0.85; }
  .stop-blue-deep { stop-color: var(--ray-blue-deep); stop-opacity: 0.9; }
  .stop-blue-clear { stop-color: var(--ray-blue); stop-opacity: 0; }
  .stop-sepia { stop-color: var(--paper-sepia); stop-opacity: 0.45; }
  .stop-sepia-clear { stop-color: var(--paper-sepia); stop-opacity: 0; }
  .paper-rim {
    fill: none;
    stroke: var(--edge-rim);
    stroke-width: 3;
    stroke-linejoin: round;
  }
</style>
</head>
<body>
  <main class="flyer-page">
    <svg class="vintage-half" viewBox="0 0 620 756" width="620" height="756"
         role="img" aria-label="Aged cream paper with faded blue swirling sunburst rays, torn roughly along the right edge">
      <defs>
        <path id="tornOutline" d="
          M0,0 L590,0 L593,6 L591,14 L595,19 L592,27 L594,38 L591,47 L596,55 L593,63
          L595,76 L592,88 L597,96 L594,104 L596,119 L593,131 L595,140 L598,147 L594,158
          L596,172 L600,178 L597,186 L595,199 L597,214 L594,226 L596,241 L593,252 L596,266
          L594,279 L597,291 L595,303 L598,316 L595,330 L597,343 L594,356 L597,371 L595,384
          L598,398 L596,410 L599,419 L597,433 L599,447 L596,461 L598,476 L596,489 L599,503
          L597,517 L600,528 L597,542 L599,556 L596,570 L599,584 L597,597 L600,611 L598,624
          L600,637 L597,650 L600,663 L598,677 L601,691 L599,703 L602,717 L600,729 L603,741
          L601,750 L604,756 L0,756 Z"/>
        <radialGradient id="paperBase" cx="0.62" cy="0.52" r="0.75">
          <stop offset="0" class="stop-light"/>
          <stop offset="0.6" class="stop-cream"/>
          <stop offset="1" class="stop-warm"/>
        </radialGradient>
        <radialGradient id="blueTopLeft" cx="0.05" cy="0.05" r="0.75">
          <stop offset="0" class="stop-blue-deep"/>
          <stop offset="0.55" class="stop-blue"/>
          <stop offset="1" class="stop-blue-clear"/>
        </radialGradient>
        <radialGradient id="blueBottom" cx="0.35" cy="1" r="0.5">
          <stop offset="0" class="stop-blue"/>
          <stop offset="1" class="stop-blue-clear"/>
        </radialGradient>
        <radialGradient id="blueLeft" cx="0" cy="0.7" r="0.45">
          <stop offset="0" class="stop-blue"/>
          <stop offset="1" class="stop-blue-clear"/>
        </radialGradient>
        <linearGradient id="agedEdge" x1="0" y1="0" x2="1" y2="0">
          <stop offset="0.82" class="stop-sepia-clear"/>
          <stop offset="1" class="stop-sepia"/>
        </linearGradient>
        <radialGradient id="agedCorner" cx="1" cy="1" r="0.4">
          <stop offset="0" class="stop-sepia"/>
          <stop offset="1" class="stop-sepia-clear"/>
        </radialGradient>
        <clipPath id="paperClip"><use href="#tornOutline"/></clipPath>
      </defs>
      <g class="torn-paper" clip-path="url(#paperClip)">
        <rect width="620" height="756" fill="url(#paperBase)"/>
        <rect width="620" height="756" fill="url(#blueTopLeft)"/>
        <rect width="620" height="756" fill="url(#blueLeft)"/>
        <rect width="620" height="756" fill="url(#blueBottom)"/>
        <rect width="620" height="756" fill="url(#agedEdge)"/>
        <rect width="620" height="756" fill="url(#agedCorner)"/>
      </g>
      <use class="paper-rim" href="#tornOutline" clip-path="url(#paperClip)"/>
    </svg>
  </main>
</body>
</html>
```